Hollowmere Farm Promotional Leaflet

The team at Hollowmere Farm can help with every aspect of managing and enhancing your home from housekeeping and professional cleaning, laundry and ironing to providing chic and contemporary flower arrangements and even food for your pets!We take pride in providing high-end, consistent and reliable professional services bespoke to you. Whether you are a busy professional working long hours, a stay-at home parent or retired; having professional help in the home gives you time to spend on the things you enjoy.We are providing a very upmarket, highly professional service and need an A5 promotional leaflet to be designed. Please refer to www.hollowmerefarm-example.co.uk and see the section on 'Home Management'The leaflet should incorporate the Hollowmere Farm logo without the 'tipi', and any suitable photography images used on the home page of the website or the 'home management' section.

Target Market(s)

high-end, affluent owners of luxury homes

Industry/Entity Type

Farm

Contact Information for Business Card

The business card design needs to be suitable for use across all of Hollowmere Farm businesses, specifically:
Hollowmere Farm Home Management - otherwise known as Hollowmere Farm @ Home (this uses the typographical logo
Hollowmere Farm Weddings & Events - this uses the 'tipi' logo

Requirements
Must have
• Design in keeping with the look and feel of the logo and website design
• www.hollowmerefarm-example.co.uk

```html
<!DOCTYPE html>
<html lang="en">
<head>
<meta charset="utf-8">
<title>Hollowmere Farm Home Management Leaflet</title>
<link href="https://fonts.googleapis.com/css2?family=Cormorant+Garamond:ital,wght@0,600;1,500&family=Montserrat:wght@400;500&display=swap" rel="stylesheet">
<style>
  :root {
    --magenta: #e2087f;
    --ink: #1f1f1f;
    --paper: #ffffff;
    --backdrop: #efe9e2;
  }
  * { box-sizing: border-box; margin: 0; padding: 0; }
  html, body { width: 992px; height: 1200px; overflow: hidden; background: var(--backdrop); }
  .leaflet {
    position: absolute; left: 86px; top: 20px; width: 820px; height: 1160px;
    display: flex; flex-direction: column;
    background: var(--paper); font-family: "Montserrat", sans-serif; color: var(--ink);
    box-shadow: 0 2px 10px rgba(0,0,0,.12);
  }
  .masthead {
    flex: 0 0 130px; background: var(--magenta);
    display: flex; align-items: center; padding-left: 60px; gap: 16px;
  }
  .masthead .mark { width: 14px; height: 14px; border-radius: 50%; background: var(--paper); }
  .masthead .brand {
    font-family: "Cormorant Garamond", serif; font-weight: 600; font-size: 56px;
    color: var(--paper); letter-spacing: 1px;
  }
  .section { padding: 0 60px; }
  .section-title {
    display: flex; align-items: center; gap: 20px; margin: 26px 0 20px;
    font-family: "Cormorant Garamond", serif; font-style: italic; font-weight: 500;
    color: var(--magenta); font-size: 34px; line-height: 1.05; text-align: center;
  }
  .section-title::before, .section-title::after {
    content: ""; flex: 1; height: 2px; background: var(--magenta);
  }
  .section-row { display: flex; gap: 30px; align-items: flex-start; }
  .photo { flex: 0 0 310px; }
  .photo-home { height: 290px; background: linear-gradient(150deg, #e9e9ea 0%, #bfc1c6 45%, #1c2350 100%); }
  .photo-interior { height: 330px; background: linear-gradient(160deg, #3a3329 0%, #b9ad98 45%, #e6ded0 70%, #4a4237 100%); }
  .copy { flex: 1; font-size: 14px; line-height: 1.4; }
  .copy p { margin-bottom: 10px; }
  .bullets { list-style: none; }
  .bullets li { position: relative; padding-left: 22px; margin-bottom: 5px; }
  .bullets li::before {
    content: ""; position: absolute; left: 2px; top: 6px; width: 7px; height: 7px;
    border-radius: 50%; background: var(--magenta);
  }
  .closing { margin-top: 12px; }
  .contact {
    margin-top: auto; padding: 0 60px 22px;
    display: flex; justify-content: space-between; gap: 16px;
    font-size: 13px; white-space: nowrap;
  }
  .contact .label { color: var(--magenta); margin-right: 4px; }
  .footer-band { flex: 0 0 36px; background: var(--magenta); }
</style>
</head>
<body>
<main class="leaflet">
  <header class="masthead">
    <span class="mark"></span>
    <span class="brand">Hollowmere Farm</span>
  </header>

  <section class="section">
    <h2 class="section-title">Hollowmere<br>Farm Home Management</h2>
    <div class="section-row">
      <div class="photo photo-home" role="img" aria-label="Photo of a woman relaxing with her dog on a navy sofa in a bright living room"></div>
      <div class="copy">
        <p>The team @ Hollowmere Farm can help with every aspect of managing and enhancing your home including:</p>
        <ul class="bullets">
          <li>Regular housekeeping and professional cleaning</li>
          <li>Exit cleans</li>
          <li>One-off seasonal / party / building work cleans</li>
          <li>Laundry and ironing</li>
          <li>Chic and contemporary flower arrangements</li>
          <li>Car valeting</li>
          <li>Pet food delivery</li>
          <li>Dry cleaning</li>
        </ul>
      </div>
    </div>
  </section>

  <section class="section">
    <h2 class="section-title">Professional Cleaning Services</h2>
    <div class="section-row">
      <div class="photo photo-interior" role="img" aria-label="Photo of a luxurious hallway with mirrors, chandeliers and white flowers"></div>
      <div class="copy">
        <p>We take pride in providing high-end, consistent and reliable professional services bespoke to you.</p>
        <p>Coming home to a beautiful environment and being able to relax and enjoy your time is something we all deserve.</p>
        <ul class="bullets">
          <li>Satisfaction guaranteed</li>
          <li>Professional staff you can trust and rely on</li>
          <li>Competitive rates</li>
          <li>CRB checked and referenced</li>
          <li>Member of the Domestic Staffing Guild</li>
          <li>Fully insured</li>
        </ul>
        <p class="closing">We look after our clients' homes and holiday lets across South Somerset. Contact us to arrange a home visit and quotation:</p>
      </div>
    </div>
  </section>

  <footer class="contact">
    <span><span class="label">E:</span>info@hollowmerefarm-example.co.uk</span>
    <span><span class="label">T:</span>07700 900123</span>
    <span><span class="label">W:</span>www.hollowmerefarm-example.co.uk</span>
  </footer>
  <div class="footer-band"></div>
</main>
</body>
</html>
```